Etikett für Likörflasche - Moonshine
Zielgruppe
Wir sind eine kleine Moonshine / Likörmanufaktur. Unser Obst für die Brände und Liköre stammt aus eigenem Anbau bzw. von umliegenden regionalen Bauern. Hier setzen wir auf sehr gute Qualität und verwenden keine Zusatzstoffe, Geschmacksverstärker, Farbstoffe etc. Im ersten Schritt werden wir nur 3-4 verschiedene Liköre anbieten.
Wir möchten unsere Liköre zukünftig auf Veranstaltungen / Events und Märkten verkaufen. Hierfür suchen wir ein pfiffiges und ansprechendes Etikettendesign.
Das Wort 'Moonshine' soll die Leute auf den Events zu uns führen. Das wird auch mit großen Fahnen am Verkaufsstand beworben. Da wir auch ein paar amerikanische Foodtrucks haben soll auch das Etikett ein bisschen amerikanisch gehalten werden.
Zielgruppe: 28 bis 55 Jahre (Männer & Frauen)
Verkaufspreis pro 0,5 Liter Flasche ca. 24,50 Euro
Aufgabenstellung
Es soll ein Etikett auf die Flasche (nur vorne nicht auf die Rückseite).
Etikettengröße: ca. 7,0 x 8,5cm (für die 0,5l Flasche)
Angaben die sich auf dem Etikett ändern:
- Inhalt entweder 0,35l oder 0,5l Flasche
- Bezeichnung vom Inhalt und 'Kurzbeschreibung'
- Alkoholgehalt
Ich habe in PowerPoint schon mal ein Etikett zusammen gestellt, auf dem die Angaben alle mit enthalten sind. Hier fehlt mir allerdings der Pfiff und das Professionelle. Auch die Darstellung der Eigenschaften wie 'Echte Früchte', 'Handcrafted' etc. gefällt mir so auch nicht. Vielleicht wäre auch noch ein cooler Spruch darauf gut.
In die Anlage habe ich meine kreierte PowerPoint Folie gepackt (auf der 2. Folie findet ihr die geplante Flasche in die abgefüllt wird). Die zweite Datei ist ein Design was meinen Vorstellungen schon gut nahe kommt aus dem Internet (hier gefallen mir die Linien, kleine Gimmicks etc. da passiert einfach was auf dem Etikett). Von der Art her würde mir dieser Style gut gefallen. Es soll nur nicht zu überladen und kitschig werden.
Likörsorten die es geben wird: Wir werden uns erstmal auf 3-4 Sorten beschränken.

```html
<!DOCTYPE html>
<html lang="de">
<head>
<meta charset="utf-8">
<title>Hollow Creek Moonshine – Etikett</title>
<link rel="stylesheet" href="https://fonts.googleapis.com/css2?family=Oswald:wght@500;600&family=Yellowtail&family=Caveat+Brush&family=Montserrat:wght@300;600&display=block">
<style>
  :root{
    --bg-top:#c7d5e4;
    --bg-bottom:#93a7d4;
    --label-navy:#2a2a54;
    --ink-white:#ffffff;
    --ink-yellow:#f0df72;
    --ink-red:#c21f24;
    --ink-lilac:#c9c4d8;
    --caption:#3a3a3f;
  }
  *{margin:0;padding:0;box-sizing:border-box}
  html,body{width:1200px;height:2400px;overflow:hidden}
  body{background:linear-gradient(180deg,var(--bg-top),var(--bg-bottom));position:relative;font-family:'Oswald',sans-serif}
  .label{position:absolute;left:160px;top:420px;width:880px;height:1069px;background:var(--label-navy);overflow:hidden}
  .label > *{position:absolute}
  .frame{left:0;top:0;width:880px;height:1069px}
  .corner-star{width:56px;height:56px}
  .corner-star--left{left:26px;top:30px}
  .corner-star--right{left:792px;top:30px}
  .hand{font-family:'Caveat Brush',sans-serif;line-height:1;text-transform:uppercase}
  .tagline-famous{left:118px;top:118px;font-size:50px;color:var(--ink-yellow);transform:rotate(-12deg);transform-origin:left bottom}
  .shooting-star{left:478px;top:130px;width:294px;height:98px;background:linear-gradient(200deg,rgba(201,196,216,0),var(--ink-lilac));border-radius:50px 10px 10px 50px;transform:rotate(-8deg)}
  .brand{left:0;width:880px;text-align:center;color:var(--ink-white);font-weight:600;text-transform:uppercase;line-height:1}
  .brand-top{top:212px;font-size:56px;letter-spacing:6px}
  .brand-main{top:276px;font-size:140px;letter-spacing:4px}
  .specs{left:144px;width:609px;top:436px;display:flex;justify-content:space-around;font-size:34px;font-weight:500;color:var(--ink-white)}
  .rule{left:144px;width:609px;height:2px;background:var(--ink-white)}
  .rule--top{top:489px}
  .rule--bottom{top:630px}
  .product-name{left:0;width:880px;top:494px;text-align:center;font-family:'Yellowtail','Caveat Brush',cursive;font-weight:400;font-size:96px;color:var(--ink-yellow);line-height:1.05}
  .product-sub{left:0;width:880px;top:592px;text-align:center;font-family:'Caveat Brush',sans-serif;font-size:30px;color:var(--ink-yellow)}
  .description{left:0;width:880px;top:648px;text-align:center;font-size:33px;font-weight:500;color:var(--ink-white);line-height:1.4;text-transform:uppercase}
  .claim-handcrafted{left:180px;top:760px;font-size:44px;color:var(--ink-yellow);transform:rotate(-14deg);line-height:.95}
  .claim-additives{left:500px;top:780px;font-size:44px;color:var(--ink-yellow);transform:rotate(9deg)}
  .address{left:0;width:880px;top:862px;text-align:center;font-size:30px;font-weight:500;color:var(--ink-white);line-height:1.2;text-transform:uppercase}
  .web{left:0;width:880px;top:986px;text-align:center;font-size:32px;font-weight:500;color:var(--ink-white);text-transform:uppercase}
  .slogan-real{left:24px;top:905px;font-size:66px;color:var(--ink-red);line-height:.95}
  .slogan-one{left:736px;top:893px;font-size:48px;color:var(--ink-red);line-height:.98}
  .caption{position:absolute;left:160px;top:1540px;font-family:'Montserrat',sans-serif;font-weight:300;font-size:68px;color:var(--caption)}
  .font-list{position:absolute;left:160px;top:1720px;font-family:'Montserrat',sans-serif;font-weight:300;font-size:30px;line-height:1.45;color:var(--caption)}
  .font-list strong{font-weight:600}
</style>
</head>
<body>
  <section class="label" aria-label="Flaschenetikett Hollow Creek Moonshine">
    <svg class="frame" viewBox="0 0 880 1069" aria-hidden="true">
      <path d="M118 84 H762 Q764 122 800 126 L768 950 Q736 952 734 982 H146 Q144 952 112 950 L80 126 Q116 122 118 84 Z" fill="none" stroke="#ffffff" stroke-width="3"/>
    </svg>
    <svg class="corner-star corner-star--left" viewBox="0 0 24 24" aria-hidden="true"><path d="M12 2 L14.6 9 L22 9 L16 13.6 L18.3 21 L12 16.5 L5.7 21 L8 13.6 L2 9 L9.4 9 Z" fill="none" stroke="#f0df72" stroke-width="1.8" stroke-linejoin="round"/></svg>
    <svg class="corner-star corner-star--right" viewBox="0 0 24 24" aria-hidden="true"><path d="M12 2 L14.6 9 L22 9 L16 13.6 L18.3 21 L12 16.5 L5.7 21 L8 13.6 L2 9 L9.4 9 Z" fill="none" stroke="#f0df72" stroke-width="1.8" stroke-linejoin="round"/></svg>

    <p class="hand tagline-famous">The Famous</p>
    <div class="shooting-star" role="img" aria-label="Gezeichnete Sternschnuppe"></div>

    <p class="brand brand-top">Hollow Creek</p>
    <h1 class="brand brand-main">Moonshine</h1>

    <div class="specs"><span>500 ML</span><span>22 % VOL.</span><span>44 PROOF</span></div>
    <div class="rule rule--top"></div>
    <h2 class="product-name">Ember and Berry</h2>
    <p class="product-sub">Seasoned Fruits</p>
    <div class="rule rule--bottom"></div>

    <p class="description">Wilde Beeren treffen auf vielschichtige<br>Noten von Whiskey und Karamell</p>

    <p class="hand claim-handcrafted">Complete<br>Handcrafted</p>
    <p class="hand claim-additives">No Additives</p>

    <p class="address">Hollow Creek Spirits<br>Am Lindenhang 12<br>91244 Talbach</p>
    <p class="web">www.hollowcreek-spirits.de</p>

    <p class="hand slogan-real">Real<br>Taste</p>
    <p class="hand slogan-one">The<br>One &amp;<br>Only</p>
  </section>

  <p class="caption">Label 7 x 8,5 cm</p>
  <p class="font-list"><strong>Verwendete Schriften:</strong><br>Soft Breeze Regular<br>Scribble Hand Regular<br>The Wanderer</p>
</body>
</html>
```